Velquora - Label design for a supplement with probiotic and prebiotic

Hello, we are a supplement company and we need a label design for our first product. The product's name is Velquora and the company's name is Toskarend Nutrition (Logo attached, It is allowed to change the color) and we are located in Orlando, if we like the label, in the future we can make other products too.
Our product is a supplement that contains probiotics, prebiotics and other vitamins, it will be packaged in a 300g plastic jar (Img attached), we like simple but premium-looking packaging.
Below are some links to brands and products we like:
https://www.brelvomarket.example/stores/page/5D2811AC-9182-4E3A-B204-C7E613ABC1DE?ingress=2&visitId=81d3eab2-1c7f-4b2e-9a01-c3f5e2d7a614&ref_=bl_dp_s_web_28351704822
https://www.brelvomarket.example/stores/page/71AB3E9D-62C4-4B17-93AA-5DE208153B81?ingress=2&visitId=6519e7ab-204c-4d8e-b3f1-7a2c90d4e1f3&ref_=bl_dp_s_web_24719032855
https://www.brelvomarket.example/stores/Quillden+Nutrition/page/C2819043-7E61-4B35-91D4-28817C03E59A?store_ref=SLP_FW_438E21DA-B91C-4A56-C88B-5213A7F0C6E2
https://www.brelvomarket.example/stores/page/EE4A17BD-29C3-4D11-A572-6BCCFA38419D?ingress=2&visitId=19b3e702-4a5d-4f8c-bd21-c8e304a7d916&ref_=bl_dp_s_web_8412093577
https://www.brelvomarket.example/stores/node/29374015822?_encoding=UTF8&field-lbr_brands_browse-bin=GLOWPATHNUTRITION&ref_=bl_dp_s_web_29374015822
https://www.brelvomarket.example/stores/page/526FA184-3307-4C29-B7D1-E9A3C28B06F1?ingress=6&visitId=4a19c6d3-8e27-4b01-a5f3-1d6b93e7c024&store_ref=storeRecs_Instant_27319388144
Hi, This product will be packaged in a 300g bottle, it is allowed to insert images and it is very important to inform "100 Billion live bacteria", 5 grams of probiotic, 5 grams of prebiotic and orange flavor.
The bottle is rounded, the size of the art must be 2.87 in and 10.74 in, I will need barcode space, supplement facts, directions and warning. This information I can put later.
Target Market(s)
Our target is people who wish to have a healthier recovery after undergoing cancer treatments, helping to maintain health, improving quality of life and reducing the harm that these treatments cause.
Requirements
Must have
- It is very important that the product contains the following information:
- 100 Billion live bacteria
- 5 grams of probiotic and 5 grams of prebiotic
- No artificial flavours
- Space for barcode
Amount per container: 10.6 oz (300 g)
Serving size: 1 scoop (10 grams)
Servings per container: 30
Amount per serving
Calories 15 Calories from fat 0
Total Fat 0
Total Carbohydrate 5g
Dietary fiber 4g
Sugars 1g
Protein 0g
Proprietary Probiotic blend: 5 billons
Lactobacillus acidophilus
Bifidobacterium animalis subsp. lactis.
Other ingredients: Organic inulin fiber, stevia, natural orange flavor, citric acid, riboflavin Not a significant source of cholesterol, fat and protein
Nice to have
- We like simple design
Should not have
- Images from vintaro pictures.

```html
<!DOCTYPE html>
<html lang="en">
<head>
<meta charset="utf-8">
<title>Velquora Dietary Supplement – Label Colourways</title>
<link rel="stylesheet" href="https://fonts.googleapis.com/css2?family=Josefin+Sans:wght@400&family=Oswald:wght@500;700&family=Montserrat:wght@600;700&display=swap">
<style>
  :root {
    --page-bg: #eceef4;
    --white: #ffffff;
    --brand-grey: #4a4a4c;
    --green: #56b56f;
    --green-dark: #2f7a47;
    --green-pattern: #a9d9b4;
    --teal: #10807c;
    --teal-dark: #073f40;
    --teal-pattern: #3f9f8f;
    --teal-light: #63b9b2;
    --mint: #62bd7d;
    --mint-light: #8fd3a0;
  }

  * { box-sizing: border-box; margin: 0; padding: 0; }

  html, body {
    width: 1200px;
    height: 850px;
    overflow: hidden;
    background: var(--page-bg);
  }

  .colourways {
    position: relative;
    width: 1200px;
    height: 850px;
    display: flex;
    justify-content: center;
    align-items: center;
    gap: 80px;
  }

  .label {
    position: relative;
    width: 480px;
    height: 424px;
    overflow: hidden;
    background: var(--label-bg);
    color: var(--label-ink);
  }

  .label--green {
    --label-bg: var(--green);
    --label-ink: var(--teal);
    --edge: var(--green-dark);
    --pattern: var(--green-pattern);
    --ribbon: var(--teal);
    --ribbon-fold: var(--teal-light);
    --icon-bg: var(--teal);
    --icon-ink: var(--green);
  }

  .label--teal {
    --label-bg: var(--teal);
    --label-ink: var(--white);
    --edge: var(--teal-dark);
    --pattern: var(--teal-pattern);
    --ribbon: var(--mint);
    --ribbon-fold: var(--mint-light);
    --icon-bg: var(--white);
    --icon-ink: var(--teal);
  }

  .edge {
    position: absolute;
    top: 0;
    width: 14px;
    height: 100%;
    background: var(--edge);
  }
  .edge--left { left: 0; }
  .edge--right { right: 0; }

  .pattern {
    position: absolute;
    top: 34px;
    height: 139px;
    background: var(--pattern);
  }
  .pattern--left { left: 0; width: 83px; }
  .pattern--right { left: 384px; width: 96px; }

  .brand-panel {
    position: absolute;
    left: 83px;
    top: 0;
    width: 301px;
    height: 173px;
    background: var(--white);
    display: flex;
    flex-direction: column;
    align-items: center;
    padding-top: 34px;
    font-family: "Josefin Sans", sans-serif;
    font-weight: 400;
    color: var(--brand-grey);
  }

  .brand-mark {
    width: 40px;
    height: 40px;
    background: var(--teal);
    margin-bottom: 14px;
  }

  .brand-name {
    font-size: 25px;
    letter-spacing: 2px;
    line-height: 1;
  }

  .brand-sub {
    font-size: 13px;
    letter-spacing: 9.5px;
    margin-top: 6px;
    margin-right: -9.5px;
    line-height: 1;
  }

  .shapes {
    position: absolute;
    inset: 0;
  }
  .shapes .ribbon { fill: var(--ribbon); }
  .shapes .ribbon-fold { fill: var(--ribbon-fold); }
  .shapes .arch { fill: var(--white); }

  .product-title {
    position: absolute;
    left: 62px;
    top: 176px;
    width: 343px;
    text-align: center;
    color: var(--white);
    font-family: "Oswald", sans-serif;
    text-transform: uppercase;
    line-height: 1;
  }
  .product-name {
    font-weight: 700;
    font-size: 44px;
    letter-spacing: 2px;
  }
  .product-type {
    font-weight: 500;
    font-size: 26px;
    margin-top: 2px;
    transform: scaleX(0.9);
  }

  .claims {
    position: absolute;
    left: 0;
    top: 306px;
    width: 480px;
    list-style: none;
    display: flex;
    flex-wrap: wrap;
    justify-content: center;
    row-gap: 8px;
    column-gap: 10px;
    padding: 0 64px;
  }

  .claim {
    display: flex;
    align-items: center;
    gap: 4px;
    font-family: "Montserrat", sans-serif;
    font-weight: 600;
    font-size: 11.5px;
    line-height: 1.15;
    text-transform: uppercase;
  }

  .claim-icon {
    width: 24px;
    height: 24px;
    flex: none;
  }
  .claim-icon .disc { fill: var(--icon-bg); }
  .claim-icon .mark { fill: var(--icon-ink); stroke: var(--icon-ink); }

  .claim-figure {
    font-family: "Oswald", sans-serif;
    font-weight: 500;
    font-size: 32px;
    line-height: 1;
    letter-spacing: -0.5px;
  }

  .net-weight {
    position: absolute;
    left: 183px;
    top: 391px;
    width: 100px;
    height: 20px;
    display: flex;
    align-items: center;
    justify-content: center;
    font-family: "Montserrat", sans-serif;
    font-weight: 700;
    font-size: 7.5px;
    color: var(--white);
  }
  .label--green .net-weight { background: var(--teal); }
</style>
</head>
<body>
<main class="colourways">

  <article class="label label--green" aria-label="Velquora label, green colourway">
    <div class="edge edge--left"></div>
    <div class="edge edge--right"></div>
    <div class="pattern pattern--left" role="img" aria-label="Decorative botanical leaf and flower pattern"></div>
    <div class="pattern pattern--right" role="img" aria-label="Decorative botanical leaf and flower pattern"></div>

    <div class="brand-panel">
      <span class="brand-mark"></span>
      <span class="brand-name">TOSKAREND</span>
      <span class="brand-sub">NUTRITION</span>
    </div>

    <svg class="shapes" viewBox="0 0 480 424" aria-hidden="true">
      <path class="arch" d="M130 258 Q233 342 336 258 Z"/>
      <polygon class="ribbon" points="62,173 405,173 388,216 405,260 62,260 80,216"/>
      <polygon class="ribbon-fold" points="62,173 88,173 88,260 62,260 80,216"/>
      <polygon class="ribbon-fold" points="380,173 405,173 388,216 405,260 380,260"/>
    </svg>

    <h1 class="product-title">
      <span class="product-name">VELQUORA</span><br>
      <span class="product-type">Dietary Supplement</span>
    </h1>

    <ul class="claims">
      <li class="claim">
        <svg class="claim-icon" viewBox="0 0 24 24" aria-hidden="true"><circle class="disc" cx="12" cy="12" r="8"/><circle class="mark" cx="10" cy="10" r="1.6"/><circle class="mark" cx="14" cy="14" r="1.4"/><path class="disc" d="M12 1v3M12 20v3M1 12h3M20 12h3M4 4l2 2M18 18l2 2M4 20l2-2M18 6l2-2" stroke="var(--icon-bg)" stroke-width="1.6"/></svg>
        <span class="claim-figure">100</span>
        <span>Billion<br>Live Bacteria</span>
      </li>
      <li class="claim">
        <svg class="claim-icon" viewBox="0 0 24 24" aria-hidden="true"><circle class="disc" cx="12" cy="12" r="11"/><circle class="mark" cx="8" cy="8" r="1.5"/><circle class="mark" cx="14" cy="7" r="1.3"/><circle class="mark" cx="16" cy="13" r="1.5"/><circle class="mark" cx="9" cy="14" r="1.4"/><circle class="mark" cx="12" cy="18" r="1.3"/></svg>
        <span class="claim-figure">5</span>
        <span>Grams Pro<br>&amp; Prebiotic</span>
      </li>
      <li class="claim">
        <svg class="claim-icon" viewBox="0 0 24 24" aria-hidden="true"><circle class="disc" cx="12" cy="12" r="11"/><path class="mark" d="M12 5 L17 11 A5 5 0 1 1 7 11 Z"/></svg>
        <span class="claim-figure">NO</span>
        <span>Add<br>Colors</span>
      </li>
      <li class="claim">
        <svg class="claim-icon" viewBox="0 0 24 24" aria-hidden="true"><circle class="disc" cx="12" cy="12" r="11"/><circle cx="12" cy="12" r="8" fill="none" class="mark" stroke-width="1.2" style="fill:none"/><path class="mark" d="M12 4v16M4 12h16M6.3 6.3l11.4 11.4M6.3 17.7l11.4-11.4" stroke-width="1.2" fill="none"/></svg>
        <span>Orange<br>Flavor</span>
      </li>
    </ul>

    <p class="net-weight">Net Wt.14.5oz (411g)</p>
  </article>

  <article class="label label--teal" aria-label="Velquora label, teal colourway">
    <div class="edge edge--left"></div>
    <div class="edge edge--right"></div>
    <div class="pattern pattern--left" role="img" aria-label="Decorative botanical leaf and flower pattern"></div>
    <div class="pattern pattern--right" role="img" aria-label="Decorative botanical leaf and flower pattern"></div>

    <div class="brand-panel">
      <span class="brand-mark"></span>
      <span class="brand-name">TOSKAREND</span>
      <span class="brand-sub">NUTRITION</span>
    </div>

    <svg class="shapes" viewBox="0 0 480 424" aria-hidden="true">
      <path class="arch" d="M130 258 Q233 342 336 258 Z"/>
      <polygon class="ribbon" points="62,173 405,173 388,216 405,260 62,260 80,216"/>
      <polygon class="ribbon-fold" points="62,173 88,173 88,260 62,260 80,216"/>
      <polygon class="ribbon-fold" points="380,173 405,173 388,216 405,260 380,260"/>
    </svg>

    <h1 class="product-title">
      <span class="product-name">VELQUORA</span><br>
      <span class="product-type">Dietary Supplement</span>
    </h1>

    <ul class="claims">
      <li class="claim">
        <svg class="claim-icon" viewBox="0 0 24 24" aria-hidden="true"><circle class="disc" cx="12" cy="12" r="8"/><circle class="mark" cx="10" cy="10" r="1.6"/><circle class="mark" cx="14" cy="14" r="1.4"/><path class="disc" d="M12 1v3M12 20v3M1 12h3M20 12h3M4 4l2 2M18 18l2 2M4 20l2-2M18 6l2-2" stroke="var(--icon-bg)" stroke-width="1.6"/></svg>
        <span class="claim-figure">100</span>
        <span>Billion<br>Live Bacteria</span>
      </li>
      <li class="claim">
        <svg class="claim-icon" viewBox="0 0 24 24" aria-hidden="true"><circle class="disc" cx="12" cy="12" r="11"/><circle class="mark" cx="8" cy="8" r="1.5"/><circle class="mark" cx="14" cy="7" r="1.3"/><circle class="mark" cx="16" cy="13" r="1.5"/><circle class="mark" cx="9" cy="14" r="1.4"/><circle class="mark" cx="12" cy="18" r="1.3"/></svg>
        <span class="claim-figure">5</span>
        <span>Grams Pro<br>&amp; Prebiotic</span>
      </li>
      <li class="claim">
        <svg class="claim-icon" viewBox="0 0 24 24" aria-hidden="true"><circle class="disc" cx="12" cy="12" r="11"/><path class="mark" d="M12 5 L17 11 A5 5 0 1 1 7 11 Z"/></svg>
        <span class="claim-figure">NO</span>
        <span>Add<br>Colors</span>
      </li>
      <li class="claim">
        <svg class="claim-icon" viewBox="0 0 24 24" aria-hidden="true"><circle class="disc" cx="12" cy="12" r="11"/><circle cx="12" cy="12" r="8" class="mark" stroke-width="1.2" style="fill:none"/><path class="mark" d="M12 4v16M4 12h16M6.3 6.3l11.4 11.4M6.3 17.7l11.4-11.4" stroke-width="1.2" fill="none"/></svg>
        <span>Orange<br>Flavor</span>
      </li>
    </ul>

    <p class="net-weight">Net Wt.14.5oz (411g)</p>
  </article>

</main>
</body>
</html>
```